Tender Horizon yoga, meditation & wellness

I teach kundalini yoga and meditation classes.
I have adult beginner classes, seniors classes, family yoga classes, kids yoga classes
I also offer events like cacao ceremony, full moon ceremony, and retreats

Professional, and simple website that is easy to navigate, and easy for me to update, change.

Target Market(s)

all ages

Industry/Entity Type

Health And Wellness

Coding

Coded - Design and coding required

Number of Pages Required

5+ page

Font styles to use
Decorative

Colors
cedeed
eedded
e4daeb
fbd4d5
fee3d4

Requirements
Must have
• tabs required: about, contact, events, classes, blog,
• I would like to link my facebook page & instagram accounts to the website
Nice to have
• I would like my clients to be able to register for classes and events from my website
• I would like to have a "shop" option in the future, for some items that I have for sale

```html
<!DOCTYPE html>
<html lang="en">
<head>
<meta charset="utf-8">
<title>Tender Horizon – Kundalini Yoga &amp; Meditation</title>
<link href="https://fonts.googleapis.com/css2?family=Italianno&family=Montserrat:wght@400;500;600;700&display=swap" rel="stylesheet">
<style>
:root{
  --coral:#f19d96;
  --sky:#c6d6e8;
  --ink:#2f3238;
  --text:#55585e;
  --footer:#2b2f36;
  --white:#ffffff;
  --line:#d9d9d9;
}
*{margin:0;padding:0;box-sizing:border-box}
html,body{width:1200px;height:3495px;overflow:hidden;background:var(--white)}
body{position:relative;font-family:"Montserrat",sans-serif;color:var(--text)}
.abs{position:absolute}
.script{font-family:"Italianno",cursive;font-weight:400}

/* header */
.site-header{position:absolute;left:0;top:0;width:1200px;height:130px;z-index:5}
.brand{left:40px;top:34px;display:flex;align-items:center;gap:10px}
.brand-dot{width:14px;height:14px;border-radius:50%;background:var(--coral)}
.brand-name{font-size:19px;font-weight:600;color:var(--ink);letter-spacing:.5px}
.brand-sub{left:64px;top:66px;font-size:12px;color:var(--ink);letter-spacing:.5px}
.main-nav{left:385px;top:57px;font-size:12px;color:var(--ink)}
.main-nav a{color:inherit;text-decoration:none;position:absolute;white-space:nowrap}
.main-nav .active{color:var(--coral)}
.nav-call{color:var(--coral)!important}
.register-label{left:868px;top:46px;font-size:28px;color:var(--ink)}
.pill{position:absolute;height:34px;border-radius:17px;font-size:12px;display:flex;align-items:center;justify-content:center;font-weight:500}
.pill-outline{border:1px solid var(--line);background:var(--white);color:var(--ink)}
.pill-fill{background:var(--coral);color:var(--white)}

/* hero */
.hero-photo{left:0;top:0}
.hero-kicker{left:640px;top:262px;font-size:18px;font-weight:600;color:var(--coral)}
.hero-title{left:638px;top:292px;font-size:76px;line-height:66px;color:var(--ink);width:540px}
.btn{position:absolute;height:30px;border-radius:15px;font-size:11px;display:flex;align-items:center;justify-content:center;font-weight:500;color:var(--ink);background:var(--white);border:1px solid var(--line)}

.portrait{left:640px;top:643px;width:400px;height:397px;background:linear-gradient(160deg,#7fb0a6 0%,#cfd6d2 40%,#e7e4df 70%,#9b9a93 100%)}
.intro-title{left:145px;top:905px;font-size:72px;color:var(--ink)}
.intro-sub{left:220px;top:990px;font-size:17px;color:var(--ink)}
.intro-rule{left:80px;top:1040px;width:480px;height:1px;background:var(--line)}
.intro-body{left:240px;top:1072px;width:730px;font-size:15px;line-height:24px;color:var(--text)}
.intro-body em,.intro-small em{font-style:italic;color:var(--coral)}
.intro-small{left:240px;top:1186px;width:730px;font-size:12px;line-height:21px}

/* class section */
.classes-band{left:0;top:1382px;width:1200px;height:590px;background:var(--sky)}
.classes-kicker{left:158px;top:1466px;font-size:17px;font-weight:600;color:var(--white)}
.classes-title{left:155px;top:1486px;font-size:66px;line-height:60px;color:var(--ink)}
.classes-rule{left:145px;top:1630px;width:438px;height:1px;background:#9fb0c4}
.classes-text{left:640px;top:1498px;width:405px;font-size:12px;line-height:20px;color:var(--text)}
.classes-text p+p{margin-top:18px}

.card{position:absolute;top:1764px;width:273px;height:400px;color:var(--white);overflow:hidden}
.card-img{position:absolute;inset:0}
.card-type{position:absolute;left:30px;top:28px;font-size:30px;line-height:30px}
.card-meta{position:absolute;left:30px;top:62px;font-size:12px;font-weight:600}
.card-title{position:absolute;left:30px;bottom:48px;width:210px;font-size:17px;line-height:22px;font-weight:700}
.card-raised{box-shadow:0 22px 40px rgba(0,0,0,.25)}
.card-btn{position:absolute;left:30px;bottom:48px;height:32px;width:126px;border-radius:16px;background:var(--coral);font-size:11px;display:flex;align-items:center;justify-content:center}

/* instructor */
.pink-band{left:0;top:0}
.profile{left:468px;top:2248px}
.instr-name{left:0;top:2530px;width:1200px;text-align:center;font-size:74px;color:var(--ink)}
.instr-role{left:0;top:2618px;width:1200px;text-align:center;font-size:17px;font-weight:500;color:var(--ink)}
.instr-rule{left:478px;top:2663px;width:330px;height:1px;background:#d9827b}
.instr-col{top:2700px;width:322px;font-size:12px;line-height:21px;color:var(--ink)}

/* photo strip */
.strip{left:0;top:2952px;width:1200px;height:243px;display:flex}
.strip div{flex:1}

/* footer */
.site-footer{left:0;top:3195px;width:1200px;height:300px;background:var(--footer);color:#c9ccd1;text-align:center}
.social{position:absolute;top:80px;left:540px;display:flex;gap:30px}
.social span{width:20px;height:20px;border:2px solid #c9ccd1;border-radius:3px}
.foot-nav{position:absolute;top:137px;left:0;width:1200px;font-size:12px}
.foot-nav a{color:#c9ccd1;text-decoration:none}
.foot-nav .active{color:var(--coral)}
.foot-nav i{font-style:normal;margin:0 8px}
.foot-call{position:absolute;top:160px;left:0;width:1200px;font-size:15px;font-weight:600;color:var(--coral)}
.foot-copy{position:absolute;top:210px;left:0;width:1200px;font-size:10px;color:#9a9ea5}
</style>
</head>
<body>

<svg class="abs hero-photo" width="1200" height="900" viewBox="0 0 1200 900" role="img" aria-label="Yoga teacher in white clothes and head wrap meditating outdoors beside a frozen lake with snowy trees">
  <defs>
    <linearGradient id="sky" x1="0" y1="0" x2="1" y2="0">
      <stop offset="0" stop-color="#e8e4e8"/>
      <stop offset=".45" stop-color="#f1eff2"/>
      <stop offset="1" stop-color="#dcdde3"/>
    </linearGradient>
    <linearGradient id="trees" x1="0" y1="0" x2="0" y2="1">
      <stop offset="0" stop-color="#b9bcc6" stop-opacity="0"/>
      <stop offset=".5" stop-color="#a9adb8" stop-opacity=".75"/>
      <stop offset="1" stop-color="#d6d8de" stop-opacity=".4"/>
    </linearGradient>
    <radialGradient id="figure" cx=".5" cy=".45" r=".6">
      <stop offset="0" stop-color="#fbfafb"/>
      <stop offset=".7" stop-color="#ecebef"/>
      <stop offset="1" stop-color="#e4e2e6" stop-opacity="0"/>
    </radialGradient>
    <linearGradient id="hair" x1="0" y1="0" x2="0" y2="1">
      <stop offset="0" stop-color="#c0684a" stop-opacity=".55"/>
      <stop offset="1" stop-color="#c0684a" stop-opacity="0"/>
    </linearGradient>
  </defs>
  <rect width="1200" height="900" fill="url(#sky)"/>
  <rect x="520" y="330" width="680" height="320" fill="url(#trees)"/>
  <rect x="0" y="560" width="1200" height="160" fill="#eef0f4" opacity=".7"/>
  <ellipse cx="290" cy="420" rx="230" ry="380" fill="url(#figure)"/>
  <rect x="330" y="170" width="40" height="540" rx="20" fill="url(#hair)"/>
  <polygon points="0,880 1200,650 1200,900 0,900" fill="#ffffff"/>
</svg>

<header class="site-header">
  <div class="abs brand"><span class="brand-dot"></span><span class="brand-name">Tender Horizon</span></div>
  <div class="abs brand-sub">Kundalini Yoga &amp; Meditation</div>
  <nav class="abs main-nav">
    <a class="active" style="left:0">About</a>
    <a style="left:63px">Events</a>
    <a style="left:130px">Classes</a>
    <a style="left:203px">Blog</a>
    <a style="left:255px">Contact</a>
    <a class="nav-call" style="left:328px">Call +1 555-013-2468</a>
  </nav>
  <div class="abs script register-label">Register for</div>
  <div class="pill pill-outline" style="left:960px;top:50px;width:95px">Classes</div>
  <div class="pill pill-fill" style="left:1065px;top:50px;width:95px">Events</div>
</header>

<div class="abs hero-kicker">Mira (Jot Prem Kaur)</div>
<h1 class="abs script hero-title">the holistic “yoga of awareness”</h1>
<div class="btn" style="left:640px;top:462px;width:128px">Explore More</div>

<div class="abs portrait" role="img" aria-label="Teacher playing a crystal singing bowl indoors"></div>
<h2 class="abs script intro-title">Tender Horizon</h2>
<div class="abs intro-sub">Kundalini Yoga &amp; Meditation</div>
<div class="abs intro-rule"></div>
<p class="abs intro-body">Kundalini Yoga comes from northern India and has a centuries-long tradition. It was brought to the West by <em>Yogi Anand Dev</em> in 1968. It is a powerful yoga system that includes not only physical and meditation exercises, but also healing techniques such as <em>Sat Nam Rasayan</em> and yogic massage, nutrition and lifestyle teachings of <em>Ayurveda</em>, and yogic lifestyle.</p>
<p class="abs intro-small">The comprehensive science of Kundalini Yoga also includes <em>Numerology</em>, the large group meditation courses of <em>White Tantric Yoga</em>, the martial arts technique <em>Gotka</em>, and special pregnancy yoga and yoga for childbirth.</p>
<div class="btn" style="left:240px;top:1268px;width:128px">Discover More</div>

<section>
  <div class="abs classes-band"></div>
  <div class="abs classes-kicker">What can</div>
  <h2 class="abs script classes-title">expect in a typical<br>class?</h2>
  <div class="abs classes-rule"></div>
  <div class="abs classes-text">
    <p>A typical part of Kundalini Yoga is a dynamic or flowing exercise series, beside quiet posture-holding exercises and versatile meditations, which are often also applied to Mantra music. The life energy is brought to flow. This can lead to greater vigor and more awareness in everyday life and a more conscious and healthy dealing with one-self and others.</p>
    <p>Kundalini Yoga is not dogmatic, but impact-oriented, full of meditative elements and techniques that can be directly integrated into practical, everyday life.</p>
  </div>

  <article class="card" style="left:158px">
    <div class="card-img" role="img" aria-label="Student in a white head wrap practising yoga" style="background:linear-gradient(170deg,#6f6a66,#3c3a3a 60%,#222 100%)"></div>
    <div class="card-type script">Class</div>
    <div class="card-meta">Yoga of Awareness</div>
    <div class="card-title">Kundalini Yoga - the Yoga for everyone</div>
  </article>
  <article class="card card-raised" style="left:464px">
    <div class="card-img" role="img" aria-label="Bowls of cacao and almonds on a wooden table" style="background:linear-gradient(160deg,#5a3b2c,#8a5a3e 40%,#3e2a22 100%)"></div>
    <div class="card-type script">Event</div>
    <div class="card-meta">Dec 12, 2018 &nbsp;|&nbsp; 6:00 pm</div>
    <div class="card-title" style="bottom:92px">Cacao Ceremony and Shamanic Yoga with Mira</div>
    <div class="card-btn">Register Now!</div>
  </article>
  <article class="card" style="left:769px">
    <div class="card-img" role="img" aria-label="Hands resting in a meditation mudra" style="background:linear-gradient(170deg,#a8a39f,#6c6865 55%,#2e2c2c 100%)"></div>
    <div class="card-type script">Blog</div>
    <div class="card-meta">Oct 8, 2018 &nbsp;|&nbsp; By Admin</div>
    <div class="card-title">kundalini meditation for effective communication</div>
  </article>
</section>

<section>
  <svg class="abs pink-band" width="1200" height="2952" aria-hidden="true"><polygon points="0,2528 1200,2283 1200,2952 0,2952" fill="#f19d96"/></svg>
  <svg class="abs profile" width="264" height="264" viewBox="0 0 264 264" role="img" aria-label="Portrait of the instructor with her partner inside a star-shaped frame">
    <defs><linearGradient id="pg" x1="0" y1="0" x2="1" y2="1"><stop offset="0" stop-color="#c7b8a4"/><stop offset=".5" stop-color="#d88b6e"/><stop offset="1" stop-color="#6b625c"/></linearGradient></defs>
    <polygon points="132,0 160,50 218,28 212,88 264,112 222,150 250,206 190,206 172,264 132,226 92,264 74,206 14,206 42,150 0,112 52,88 46,28 104,50" fill="#3d3a38"/>
    <polygon points="132,22 156,62 206,46 200,96 244,116 208,148 232,194 182,196 166,244 132,212 98,244 82,196 32,194 56,148 20,116 64,96 58,46 108,62" fill="url(#pg)"/>
  </svg>
  <h2 class="abs script instr-name">Mira (Jot Prem kaur)</h2>
  <div class="abs instr-role">kundalini Yoga Instructor</div>
  <div class="abs instr-rule"></div>
  <p class="abs instr-col" style="left:240px">I have been practicing yoga for about 5 years. I began practicing Kundalini yoga 2 years ago, and it ignited a complete transformation of mind, body and spirit. I knew that I would go on to teach this lineage.</p>
  <p class="abs instr-col" style="left:640px">I'm also a nurse part time with the CHNA, my 18 years of health care experience has been invaluable. My most important job of all is wife, mother and home educator to my four daughters, ages 9-4 years.</p>
  <div class="btn" style="left:536px;top:2842px;width:128px">Read More</div>
</section>

<div class="abs strip">
  <div role="img" aria-label="Child cooking in a kitchen" style="background:linear-gradient(160deg,#8b8883,#4c4a48)"></div>
  <div role="img" aria-label="Teacher in white head wrap meditating" style="background:linear-gradient(160deg,#d9d3cc,#7a6e66)"></div>
  <div role="img" aria-label="Mother holding a baby" style="background:linear-gradient(160deg,#6e5e58,#b49f93)"></div>
  <div role="img" aria-label="Smiling woman with red hair outdoors" style="background:linear-gradient(160deg,#7aa3b8,#c98c68)"></div>
  <div role="img" aria-label="Family sharing a meal at a table" style="background:linear-gradient(160deg,#e2ddd6,#8f7f72)"></div>
</div>

<footer class="abs site-footer">
  <div class="social" aria-label="Social links"><span></span><span></span><span></span></div>
  <div class="foot-nav"><a class="active">Home</a><i>|</i><a>About</a><i>|</i><a>Events</a><i>|</i><a>Classes</a><i>|</i><a>Blog</a><i>|</i><a>Contact</a></div>
  <div class="foot-call">Call +1 555-013-2468</div>
  <div class="foot-copy">© 2018 Tender Horizon Kundalini Yoga.</div>
</footer>

</body>
</html>
```